Visitenkarten-Design Neutrale Verzollungs Agentur für den Grenzverkehr des Zollwesens
Sehr schnelle Umsetzung nach unserer Vorstellung,und sehr netter und guter Umgang in der Kominikation. tolvix hat unsere erwartung zu 100 % übertroffen.
Zielgruppe
Wir sind eine Neutrale Verzollungs Agentur für den Grenzverkehr des Zollwesens
Bluefield & Meridian Group
Wir führen für Kunden die Zollabwicklungen ab.
Seefracht - Bahnfracht-Luftfracht-LKW Fracht
Cargo - Hersteller Firmen und Endknden International
Aufgabenstellung
Rückseite sollte mitgestaltet werden

```html
<!DOCTYPE html>
<html lang="de">
<head>
<meta charset="utf-8">
<title>Grenzlauf – Visitenkarte</title>
<link href="https://fonts.googleapis.com/css2?family=Open+Sans:wght@400;600;700&display=swap" rel="stylesheet">
<style>
  :root {
    --stage: #1e2124;
    --card-dark: #27343b;
    --card-white: #ffffff;
    --ink-light: #e9eef1;
    --ink-muted: #b9c4ca;
    --brand-blue: #4b8fd6;
    --accent-strip: #a9c8ec;
    --globe-core: #8fb3a6;
    --globe-edge: #33464c;
  }
  * { margin: 0; padding: 0; box-sizing: border-box; }
  html, body { width: 1200px; height: 900px; overflow: hidden; }
  body {
    background: var(--stage);
    font-family: "Open Sans", sans-serif;
    display: flex;
    flex-direction: column;
    align-items: center;
    justify-content: center;
    gap: 48px;
  }
  .card {
    width: 600px;
    height: 343px;
    position: relative;
    overflow: hidden;
    box-shadow: 0 14px 32px rgba(0,0,0,0.45);
  }
  /* Front */
  .card-front { background: var(--card-dark); }
  .globe-area {
    position: absolute;
    left: -70px;
    top: 10px;
    width: 380px;
    height: 380px;
    border-radius: 50%;
    background: radial-gradient(circle at 38% 32%, var(--globe-core) 0%, #5f7f80 35%, var(--globe-edge) 75%, var(--card-dark) 100%);
    opacity: 0.9;
  }
  .front-brand {
    position: absolute;
    left: 330px;
    top: 96px;
    font-size: 40px;
    font-weight: 600;
    color: var(--brand-blue);
    letter-spacing: 0.5px;
  }
  .front-countries {
    position: absolute;
    right: 26px;
    bottom: 40px;
    font-size: 15px;
    font-weight: 600;
    color: var(--ink-light);
    letter-spacing: 0.3px;
  }
  /* Back */
  .card-back { background: var(--card-dark); display: flex; }
  .back-logo-panel {
    width: 40%;
    height: 100%;
    background: var(--card-white);
    display: flex;
    align-items: center;
    justify-content: center;
  }
  .back-brand {
    font-size: 30px;
    font-weight: 600;
    color: var(--brand-blue);
  }
  .accent-strip {
    width: 8px;
    height: 150px;
    background: var(--accent-strip);
    margin-top: 60px;
  }
  .back-info {
    flex: 1;
    padding: 62px 0 0 40px;
    color: var(--ink-light);
  }
  .company-line { font-size: 18px; letter-spacing: 0.3px; }
  .company-sub { font-size: 9.5px; color: var(--ink-muted); line-height: 1.3; margin-top: 2px; }
  .address { font-size: 14.5px; margin-top: 22px; line-height: 1.35; }
  .contact-list { list-style: none; margin-top: 18px; font-size: 14.5px; }
  .contact-list li { display: flex; align-items: center; gap: 14px; line-height: 1.55; }
  .contact-list svg { width: 14px; height: 14px; flex: none; }
</style>
</head>
<body>

<section class="card card-front">
  <div class="globe-area" role="img" aria-label="Globus mit Nord- und Südamerika in Grüntönen"></div>
  <div class="front-brand">Grenzlauf</div>
  <div class="front-countries">Switzerland · Germany · Denmark · France</div>
</section>

<section class="card card-back">
  <div class="back-logo-panel">
    <div class="back-brand">Grenzlauf</div>
  </div>
  <div class="accent-strip"></div>
  <div class="back-info">
    <div class="company-line">Bluefield &amp; Meridian Group</div>
    <div class="company-sub">Verkauf · Vertrieb von Handelswaren<br>&amp; Dienstleistungen</div>
    <div class="address">Lindenstieg 48 b<br>22087 Hamburg</div>
    <ul class="contact-list">
      <li>
        <svg viewBox="0 0 16 16" aria-hidden="true"><path fill="#e9eef1" d="M3 1l3 3-1.5 2a9 9 0 0 0 5.5 5.5L12 10l3 3-2 2C6.5 15 1 9.5 1 3z"/></svg>
        0400- 5512 308
      </li>
      <li>
        <svg viewBox="0 0 16 16" aria-hidden="true"><rect x="1" y="3" width="14" height="10" fill="#e9eef1"/><path d="M1 3l7 6 7-6" fill="none" stroke="#27343b" stroke-width="1.4"/></svg>
        service@grenzlauf-beispiel.de
      </li>
      <li>
        <svg viewBox="0 0 16 16" aria-hidden="true"><g fill="none" stroke="#e9eef1" stroke-width="1.2"><circle cx="8" cy="8" r="6.5"/><ellipse cx="8" cy="8" rx="3" ry="6.5"/><path d="M1.5 8h13"/></g></svg>
        www.grenzlauf-beispiel.de
      </li>
    </ul>
  </div>
</section>

</body>
</html>
```